Property Management Company Business Cards

Need business cards for a property management company located in Michigan. We manage houses for clients all over the world. Young and modern company, looking for eye catching design. Please work with the attached logo.

Industry/Entity Type

Property Management

Requirements
Must have
• Need lines for address, telephone number, fax number, web site.

Also lines for name, and job title

```html
<!DOCTYPE html>
<html lang="en">
<head>
<meta charset="utf-8">
<title>Lakeshore Harbor Management – Business Cards</title>
<link rel="stylesheet" href="https://fonts.googleapis.com/css2?family=Open+Sans:wght@400;600;700&display=swap">
<style>
  :root {
    --page-bg: #ebe7df;
    --brand-blue: #29b6e3;
    --front-deep: #17708f;
    --front-mid: #2aa5c9;
    --front-light: #5fd0ea;
    --ink-dark: #2f3133;
    --ink-grey: #5c5f62;
    --paper: #ffffff;
    --stripe-dark: #3a3c3f;
    --rule: #c9cdd0;
  }
  * { box-sizing: border-box; margin: 0; padding: 0; }
  html, body { width: 1200px; height: 902px; overflow: hidden; }
  body {
    background: var(--page-bg);
    font-family: "Open Sans", Arial, sans-serif;
    position: relative;
  }
  .card {
    position: absolute;
    top: 301px;
    width: 525px;
    height: 300px;
    border-radius: 16px;
    overflow: hidden;
    box-shadow: 0 6px 18px rgba(0,0,0,0.18);
  }

  /* Front */
  .card-front {
    left: 60px;
    background: radial-gradient(ellipse at 65% 55%, var(--front-light) 0%, var(--front-mid) 45%, var(--front-deep) 100%);
  }
  .front-watermark {
    position: absolute;
    left: 40px; top: 60px;
    width: 260px; height: 260px;
    border-radius: 50%;
    background: rgba(255,255,255,0.08);
  }
  .wordmark {
    position: absolute;
    display: flex;
    align-items: center;
    gap: 12px;
  }
  .card-front .wordmark { left: 92px; top: 112px; }
  .wordmark-dot {
    width: 38px; height: 38px;
    border-radius: 50%;
    flex: none;
  }
  .card-front .wordmark-dot { background: #6b6e70; }
  .wordmark-name {
    font-weight: 700;
    font-size: 29px;
    line-height: 1;
    letter-spacing: -0.5px;
    color: #5a5d60;
    border-left: 2px solid currentColor;
    padding-left: 8px;
  }
  .wordmark-sub {
    display: block;
    font-weight: 400;
    font-size: 13px;
    letter-spacing: 10.5px;
    margin-top: 5px;
    color: var(--paper);
  }
  .front-web {
    position: absolute;
    right: 34px; bottom: 30px;
    font-size: 17px;
    color: #163f50;
  }

  /* Back */
  .card-back { left: 615px; background: var(--paper); }
  .card-back .wordmark { left: 28px; top: 36px; }
  .card-back .wordmark-dot { background: var(--brand-blue); width: 34px; height: 34px; }
  .card-back .wordmark-name { font-size: 25px; color: var(--ink-dark); }
  .card-back .wordmark-sub { font-size: 11px; letter-spacing: 9.5px; color: var(--brand-blue); }
  .divider {
    position: absolute;
    left: 75px; top: 118px;
    width: 330px; height: 1px;
    background: linear-gradient(90deg, var(--rule), rgba(201,205,208,0));
  }
  .person {
    position: absolute;
    right: 62px; top: 36px;
    text-align: left;
  }
  .person-name {
    font-variant: small-caps;
    font-size: 19px;
    color: var(--ink-dark);
    border-bottom: 1px solid var(--ink-dark);
    padding-bottom: 1px;
  }
  .person-title { font-size: 12px; color: var(--brand-blue); margin-top: 3px; }
  .contact {
    position: absolute;
    left: 28px; bottom: 30px;
    list-style: none;
    font-size: 13.5px;
    line-height: 19px;
  }
  .contact .address { color: var(--brand-blue); }
  .contact .line { color: var(--ink-dark); display: flex; align-items: center; gap: 8px; }
  .contact svg { width: 12px; height: 12px; fill: var(--brand-blue); flex: none; }
  .edge-stripe {
    position: absolute;
    right: 0; top: 0;
    width: 18px; height: 100%;
    background: var(--stripe-dark);
  }
  .edge-stripe::after {
    content: "";
    position: absolute;
    left: 0; bottom: 0;
    width: 100%; height: 78px;
    background: var(--brand-blue);
  }
</style>
</head>
<body>
  <section class="card card-front" aria-label="Card front">
    <div class="front-watermark"></div>
    <div class="wordmark">
      <span class="wordmark-dot"></span>
      <span class="wordmark-name">LAKESHORE HARBOR<span class="wordmark-sub">MANAGEMENT</span></span>
    </div>
    <p class="front-web">www.lakeshoreharbor.example</p>
  </section>

  <section class="card card-back" aria-label="Card back">
    <div class="wordmark">
      <span class="wordmark-dot"></span>
      <span class="wordmark-name">LAKESHORE HARBOR<span class="wordmark-sub">MANAGEMENT</span></span>
    </div>
    <div class="divider"></div>
    <div class="person">
      <p class="person-name">Marco Delgado</p>
      <p class="person-title">General Manager</p>
    </div>
    <ul class="contact">
      <li class="address">4820-B Lakeview Rd. 17 #204</li>
      <li class="address">Harbor City, MI 49000</li>
      <li class="line"><svg viewBox="0 0 12 12"><path d="M2.5 0.5 L4.5 0.5 L5 3.5 L3.6 4.4 Q4.6 6.8 7.6 8.4 L8.5 7 L11.5 7.5 L11.5 9.5 Q11.5 11.5 9.5 11.5 Q1 10.5 0.5 2.5 Q0.5 0.5 2.5 0.5 Z"/></svg>(000) 555-014-2200</li>
      <li class="line"><svg viewBox="0 0 12 12"><rect x="3" y="0.5" width="6" height="3"/><rect x="0.5" y="4" width="11" height="5" rx="1"/><rect x="3" y="8" width="6" height="3.5"/></svg>(000) 555-014-2201</li>
      <li class="line"><svg viewBox="0 0 12 12"><path d="M0.5 2 H11.5 V10 H0.5 Z M1 2.5 L6 6.5 L11 2.5" stroke="#fff" stroke-width="0.8"/></svg>hello@lakeshoreharbor.example</li>
      <li class="line"><svg viewBox="0 0 12 12"><circle cx="6" cy="6" r="5.5"/><path d="M0.5 6 H11.5 M6 0.5 V11.5 M6 0.5 Q2.5 6 6 11.5 M6 0.5 Q9.5 6 6 11.5" stroke="#fff" stroke-width="0.7" fill="none"/></svg>www.lakeshoreharbor.example</li>
    </ul>
    <div class="edge-stripe"></div>
  </section>
</body>
</html>
```